Water Delivery Service Website

We are working with BrivoneÉ. They are a water delivery company and in need of a new website design.
Some sites to use for inspiration:
https://www.tesmoracrest.example/home
https://www.plimvarta.example/en/home3
https://www.quelbo.example
https://www.fandorix.example
Thank you for taking the time to consider designing a website for us. We are web developers based in Stockton, CA, USA. Most of our projects go through the same process. Understanding this process may help you win a project with us. We custom-code all of our websites in-house. We don’t have any requirements as to what tools you use for your design, but we prefer Figma files. For any design that we label as four-stars, we send it to the client for review. The client picks the final design they want us to use. Once we complete this process, we will continue to show additional clients all the four-star sites and purchase them later. Your designs will have multiple chances to sell. For better chances of success, we ask that you follow these guidelines.
IMAGES:
If you use any images or icons in the design, we ask that you have a link to the asset so we can purchase the image/icon. Most of the designs we submit do not have the customer’s images on them unless they have some great images. Be creative; show us the feeling you are trying to portray with your image choices. Use any royalty-free site you choose. We subscribe to Adobe and mainly use their images, but we can purchase images outside of Adobe.
PLEASE NOTE: we will not submit designs to clients with watermarks on the images.
FONTS:
We ask that you identify the fonts used in the design. This can be done in a message if you want. We typically use Google Fonts and Adobe Fonts.
CONTENT:
We're always open to different content and ideas. We often submit designs with stock images so the client can see our vision. We typically take pictures after the website launch to use their images with our vision. Lorem Ipsum is fine for paragraphs, but we ask that you write the headers in correct English. We want to be able to show the vision and identify the sections of the website.
INSPIRATION:
We typically add a couple of links in the brief of websites we like to help you get started in your design.
REVISIONS:
We do not often ask for revisions of the designs unless we see something in the design that may not appeal to the client. If there are slight changes that we want to make, we do that in the development process.
FEEDBACK:
We rarely give feedback on designs during the design process. We are working on many website projects and do not have the time to provide feedback. We usually respond if your request is well thought out and asks specific questions, but a note asking “feedback, please” usually goes unanswered.

```html
<!DOCTYPE html>
<html lang="en">
<head>
<meta charset="utf-8">
<title>BrivoneÉ Water Delivery</title>
<link href="https://fonts.googleapis.com/css2?family=Poppins:wght@400;500;600;700&display=swap" rel="stylesheet">
<style>
:root{
  --blue:#1ea3e6;
  --blue-deep:#1488d0;
  --navy:#1c2461;
  --ink:#111111;
  --grey:#4a4a4a;
  --pale:#dff1fa;
  --white:#ffffff;
}
*{box-sizing:border-box;margin:0;padding:0}
html,body{width:1200px;height:4648px;overflow:hidden}
body{position:relative;background:var(--white);font-family:"Poppins",sans-serif;color:var(--ink)}
.abs{position:absolute}
/* header */
.brand{left:128px;top:28px;display:flex;align-items:center;gap:12px}
.brand-dot{width:36px;height:36px;border-radius:50%;background:var(--blue)}
.brand-name{font-size:38px;font-weight:500;color:var(--blue);font-family:"Poppins",sans-serif}
.call{left:838px;top:20px;font-size:17px;font-weight:600;color:var(--blue);display:flex;align-items:center;gap:8px}
.nav{top:64px;left:0;width:1200px;height:20px}
.nav a{position:absolute;font-size:15px;font-weight:500;color:var(--ink);text-decoration:none}
.nav a.active{color:var(--blue)}
/* hero */
.hero{left:0;top:108px;width:1200px;height:612px;background:linear-gradient(110deg,#6b7a86 0%,#3a4756 40%,#1d3e6a 70%,#7fb4d8 100%)}
.hero-curve{left:0;top:560px}
.hero-title{left:124px;top:252px;font-size:46px;font-weight:600;line-height:56px;color:var(--white)}
.btn{display:flex;align-items:center;gap:12px;border-radius:30px;font-weight:600;font-size:17px;text-transform:uppercase;text-decoration:none}
.btn-dot{width:28px;height:28px;border-radius:50%;background:var(--white)}
.btn-solid{background:var(--blue);color:var(--white);border:3px solid var(--white);padding:0 26px 0 14px;height:60px}
.btn-solid .btn-dot{background:var(--white)}
/* about */
.about-photo{left:126px;top:828px;width:408px;height:408px;border-radius:50%;background:radial-gradient(circle at 50% 40%,#c9d6e0,#5b7fa6 60%,#1a6ec4)}
.h2{font-size:40px;font-weight:600;line-height:46px}
.about-title{left:581px;top:830px}
.about-text{left:581px;top:946px;width:496px;font-size:14.5px;line-height:23px;color:var(--grey)}
.about-btn{left:581px;top:1222px;height:56px}
/* what we do */
.wwd-bg{left:0;top:1390px;width:1200px;height:720px;background:linear-gradient(180deg,var(--pale) 0%,#eef8fd 60%,#ffffff 100%)}
.center-title{left:0;width:1200px;text-align:center}
.card{width:294px;background:var(--white);border-radius:18px;box-shadow:0 6px 24px rgba(30,80,130,.10);padding:16px 14px 0;text-align:center}
.card-img{height:210px;border-radius:12px}
.card h3{margin-top:22px;font-size:20px;font-weight:600;line-height:26px}
.card p{margin:22px auto 0;width:262px;font-size:14px;line-height:21px;color:var(--grey)}
.card{height:437px}
/* why */
.why-sub{left:0;width:1200px;top:2276px;text-align:center;font-size:14.5px;line-height:21px;color:var(--grey)}
.feat h4{font-size:19px;font-weight:600;color:var(--navy);margin-bottom:8px}
.feat p{font-size:13.5px;line-height:21px;color:var(--grey)}
.feat-left{width:286px;text-align:right}
.feat-right{width:260px}
.icon{width:60px;height:60px}
.core-photo{left:489px;top:2420px;width:224px;height:224px;border-radius:50%;background:radial-gradient(circle at 45% 40%,#7fb6e6,#2f6fb0 70%)}
/* delivery band */
.band{left:0;top:3045px}
.band-title{left:127px;top:3118px;font-size:42px;font-weight:600;line-height:50px;color:var(--white)}
.band-text{left:127px;top:3232px;width:400px;font-size:14.5px;line-height:23px;color:var(--white)}
.band-btn{left:127px;top:3355px;height:58px;width:308px;border:2px solid var(--white);color:var(--white);background:transparent;padding-left:14px}
/* footer */
.foot-head{font-size:17px;font-weight:600;color:var(--blue);margin-bottom:14px}
.foot-list{list-style:none;font-size:14.5px;line-height:26px;color:var(--white)}
.foot-rule{width:2px;background:rgba(255,255,255,.35)}
.foot-tick{width:4px;height:22px;background:var(--blue);border-radius:2px}
.social{width:32px;height:32px;border-radius:50%;border:2px solid var(--white)}
.copy{left:0;width:1200px;top:4588px;text-align:center;font-size:14.5px;color:var(--white)}
.contact-row{display:flex;gap:10px;font-size:14.5px;line-height:19px;color:var(--white);margin-bottom:14px}
</style>
</head>
<body>

<!-- header -->
<div class="abs brand"><span class="brand-dot"></span><span class="brand-name">BrivoneÉ</span></div>
<div class="abs call">
  <svg width="18" height="18" viewBox="0 0 24 24"><path d="M6.6 10.8c1.4 2.8 3.8 5.1 6.6 6.6l2.2-2.2c.3-.3.7-.4 1-.2 1.1.4 2.3.6 3.6.6.6 0 1 .4 1 1V20c0 .6-.4 1-1 1C10.6 21 3 13.4 3 4c0-.6.4-1 1-1h3.5c.6 0 1 .4 1 1 0 1.3.2 2.5.6 3.6.1.3 0 .7-.2 1L6.6 10.8z" fill="var(--blue)"/></svg>
  Call Us: 404 5512 318
</div>
<nav class="abs nav">
  <a class="active" style="left:519px">Home</a>
  <a style="left:612px">About</a>
  <a style="left:705px">Services</a>
  <a style="left:818px">News</a>
  <a style="left:906px">Clients</a>
  <a style="left:1007px">Contact</a>
</nav>

<!-- hero -->
<div class="abs hero" role="img" aria-label="Delivery worker carrying a large water bottle on his shoulder to a customer at the door"></div>
<svg class="abs hero-curve" width="1200" height="170" viewBox="0 0 1200 170"><path d="M0 50 C300 150 700 170 1200 50 L1200 170 L0 170 Z" fill="var(--white)"/></svg>
<h1 class="abs hero-title">BrivoneÉ Water<br>Delivery Service</h1>
<a class="abs btn btn-solid" style="left:124px;top:395px;height:60px"><span class="btn-dot"></span>Read More</a>

<!-- about -->
<div class="abs about-photo" role="img" aria-label="Worker in apron carrying a water jug in a bottling warehouse"></div>
<h2 class="abs h2 about-title">Aboout BrivoneÉ Water<br>Delivery Service</h2>
<p class="abs about-text">Lorem ipsum dolor sit amet, consectetur adipiscing elit, sed do eiusmod tempor incididunt ut labore et dolore magna aliqua. Quis ipsum suspendisse ultrices gravida. Risus commodo viverra maecenas accumsan lacus vel facilisis. Lorem ipsum dolor sit amet, consectetur adipiscing elit, sed do eiusmod tempor inci did unt ut labore et dolore magna aliqua. Quis ipsum suspe ndis se ultrices gravida. Risus commodo viverra maecenas accum san lacus vel facilisis. Lorem ipsum dolor sit amet, consectetur adipiscing elit, sed do eiusmod tempor incididunt ut labore et dolore magna aliqua. Quis ipsum suspendisse ultrices grisus commodo viverra maecenas accumsa.</p>
<a class="abs btn btn-solid about-btn"><span class="btn-dot"></span>Read More</a>

<!-- what we do -->
<div class="abs wwd-bg"></div>
<svg class="abs" style="left:0;top:1380px" width="1200" height="90" viewBox="0 0 1200 90"><path d="M0 0 L1200 0 L1200 80 C900 0 300 0 0 80 Z" fill="var(--white)"/></svg>
<h2 class="abs h2 center-title" style="top:1478px">What We Do</h2>
<div class="abs card" style="left:127px;top:1566px"><div class="card-img" role="img" aria-label="Hands placing water bottles on a production line" style="background:linear-gradient(160deg,#cfe3f0,#5fa7d8)"></div><h3>Lorem ipsum dolor<br>sit amet consect.</h3><p>Lorem ipsum dolor sit amet, consectetur adipiscing elit, sed do eiusmod tempor incididunt ut labore et dolore magna.</p></div>
<div class="abs card" style="left:452px;top:1566px"><div class="card-img" role="img" aria-label="Hand truck loaded with water jugs" style="background:linear-gradient(160deg,#a9c4d8,#3d6f98)"></div><h3>Lorem ipsum dolor<br>sit amet consect.</h3><p>Lorem ipsum dolor sit amet, consectetur adipiscing elit, sed do eiusmod tempor incididunt ut labore et dolore magna.</p></div>
<div class="abs card" style="left:776px;top:1566px"><div class="card-img" role="img" aria-label="Delivery worker lifting two water jugs outdoors" style="background:linear-gradient(160deg,#6f9a5e,#2d6fc2)"></div><h3>Lorem ipsum dolor<br>sit amet consect.</h3><p>Lorem ipsum dolor sit amet, consectetur adipiscing elit, sed do eiusmod tempor incididunt ut labore et dolore magna.</p></div>

<!-- why -->
<h2 class="abs h2 center-title" style="top:2214px">Why Our Products are Best</h2>
<p class="abs why-sub">Lorem ipsum dolor sit amet, consectetur adipiscing elit, sed do<br>eiusmod tempor incididunt ut labore et dolore magna.</p>

<svg class="abs" style="left:431px;top:2361px" width="340" height="340" viewBox="0 0 340 340">
  <circle cx="170" cy="170" r="164" fill="var(--navy)" stroke="var(--blue)" stroke-width="6"/>
  <circle cx="30" cy="71" r="8" fill="var(--blue)"/><circle cx="310" cy="71" r="8" fill="var(--blue)"/>
  <circle cx="14" cy="190" r="8" fill="var(--blue)"/><circle cx="326" cy="190" r="8" fill="var(--blue)"/>
  <circle cx="170" cy="334" r="8" fill="var(--blue)"/>
</svg>
<div class="abs core-photo" role="img" aria-label="Man drinking water from a bottle after exercise"></div>

<div class="abs feat feat-left" style="left:52px;top:2378px"><h4>Best Services</h4><p>Lorem ipsum dolor sit amet, con sectetur adipiscing elit, sed do eiusmod tempor incididunt.</p></div>
<svg class="abs icon" style="left:360px;top:2378px" viewBox="0 0 60 60" fill="none" stroke="var(--blue)" stroke-width="2"><rect x="22" y="4" width="16" height="6" rx="1"/><path d="M24 10v6l-8 6v32h28V22l-8-6v-6"/><line x1="16" y1="32" x2="44" y2="32"/><line x1="16" y1="44" x2="44" y2="44"/><circle cx="30" cy="38" r="2"/></svg>

<div class="abs feat feat-right" style="left:865px;top:2378px"><h4>Best Quality</h4><p>Lorem ipsum dolor sit amet, con sectetur adipiscing elit, sed do eiusmod tempor incididunt.</p></div>
<svg class="abs icon" style="left:778px;top:2374px" viewBox="0 0 60 60" fill="none" stroke="var(--blue)" stroke-width="2"><path d="M30 4l6 5 8-1 2 8 7 4-3 7 3 7-7 4-2 8-8-1-6 5-6-5-8 1-2-8-7-4 3-7-3-7 7-4 2-8 8 1z"/><circle cx="30" cy="30" r="14"/><path d="M23 30l5 5 9-10"/></svg>

<div class="abs feat feat-left" style="left:52px;top:2596px"><h4>Free Delivery</h4><p>Lorem ipsum dolor sit amet, con sectetur adipiscing elit, sed do eiusmod tempor incididunt.</p></div>
<svg class="abs" style="left:364px;top:2608px" width="72" height="56" viewBox="0 0 72 56" fill="none" stroke="var(--blue)" stroke-width="2"><rect x="2" y="4" width="40" height="34" rx="2"/><path d="M42 14h14l12 12v12H42"/><circle cx="16" cy="44" r="6"/><circle cx="56" cy="44" r="6"/><text x="7" y="24" font-family="Poppins,sans-serif" font-size="12" font-weight="600" fill="var(--blue)" stroke="none">FREE</text></svg>

<div class="abs feat feat-right" style="left:865px;top:2596px"><h4>Secure Payments</h4><p>Lorem ipsum dolor sit amet, con sectetur adipiscing elit, sed do eiusmod tempor incididunt.</p></div>
<svg class="abs" style="left:768px;top:2604px" width="76" height="60" viewBox="0 0 76 60" fill="none" stroke="var(--blue)" stroke-width="2"><rect x="2" y="4" width="60" height="40" rx="3"/><line x1="2" y1="14" x2="62" y2="14"/><line x1="10" y1="32" x2="30" y2="32"/><path d="M58 28l12 4v10c0 8-6 12-12 14-6-2-12-6-12-14V32z" fill="var(--white)"/><path d="M53 43l4 4 7-8"/></svg>

<svg class="abs" style="left:560px;top:2720px" width="84" height="84" viewBox="0 0 84 84" fill="none" stroke="var(--blue)" stroke-width="2"><circle cx="36" cy="38" r="12"/><path d="M20 40a16 16 0 0 1 32 0"/><rect x="16" y="38" width="6" height="10" rx="2"/><rect x="50" y="38" width="6" height="10" rx="2"/><path d="M20 70c2-10 10-14 16-14s14 4 16 14"/><rect x="52" y="6" width="26" height="16" rx="3"/><path d="M58 22l-2 6 7-6"/><path d="M10 30a30 30 0 0 1 12-20M62 66a30 30 0 0 1-14 10"/></svg>
<div class="abs feat" style="left:0;width:1200px;top:2808px;text-align:center"><h4>Support 24/7</h4><p>Lorem ipsum dolor sit amet<br>con sectetur adipiscing elit, sed do<br>eiusmod tempor incididunt.</p></div>

<!-- delivery band -->
<svg class="abs band" width="1200" height="425" viewBox="0 0 1200 425"><path d="M0 0 H860 A212 212 0 0 1 860 425 H0 Z" fill="var(--blue)"/></svg>
<div class="abs" role="img" aria-label="Smiling delivery man giving a thumbs up while carrying a water jug on his shoulder" style="left:560px;top:3045px;width:512px;height:425px;border-radius:0 212px 212px 0;background:linear-gradient(100deg,rgba(30,163,230,0) 0%,#2b86d6 45%,#5aa9e6 80%,#cfe8f6 100%)"></div>
<h2 class="abs band-title">Fastest Delivery &amp;<br>Easy Pickup</h2>
<p class="abs band-text">Lorem ipsum dolor sit amet, consectetur adipiscin elit, sed do eiusmod tempor incididunt ut labore et dolore magna aliqua. Quis ipsum suspendisse ultric es gravida. Risus commodo viverra maecenas ac cumsan lacus vel facilisis. Lorem ipsum dolo.</p>
<a class="abs btn band-btn"><span class="btn-dot"></span>Explore Our Delivery</a>

<!-- blog -->
<h2 class="abs h2 center-title" style="top:3566px">Latest Blog Post</h2>
<div class="abs card" style="left:127px;top:3658px"><div class="card-img" role="img" aria-label="Rows of stacked water jugs in a warehouse" style="background:linear-gradient(160deg,#9cc3e6,#2a62b8)"></div><h3>Lorem ipsum dolor<br>sit amet consect.</h3><p>Lorem ipsum dolor sit amet, consectetur adipiscing elit, sed do eiusmod tempor incididunt ut labore et dolore magna.</p></div>
<div class="abs card" style="left:452px;top:3658px"><div class="card-img" role="img" aria-label="Delivery worker loading water jugs into a van" style="background:linear-gradient(160deg,#2d3440,#3f7fc6)"></div><h3>Lorem ipsum dolor<br>sit amet consect.</h3><p>Lorem ipsum dolor sit amet, consectetur adipiscing elit, sed do eiusmod tempor incididunt ut labore et dolore magna.</p></div>
<div class="abs card" style="left:776px;top:3658px"><div class="card-img" role="img" aria-label="Stack of blue water jugs" style="background:linear-gradient(160deg,#b9d8ee,#3a86c8)"></div><h3>Lorem ipsum dolor<br>sit amet consect.</h3><p>Lorem ipsum dolor sit amet, consectetur adipiscing elit, sed do eiusmod tempor incididunt ut labore et dolore magna.</p></div>

<!-- footer -->
<svg class="abs" style="left:0;top:4180px" width="1200" height="468" viewBox="0 0 1200 468"><path d="M0 100 C300 -10 900 -10 1200 100 L1200 468 L0 468 Z" fill="var(--blue)"/><path d="M0 112 C300 8 900 8 1200 112 L1200 468 L0 468 Z" fill="var(--navy)"/></svg>
<div class="abs brand" style="left:132px;top:4350px"><span class="brand-dot"></span><span class="brand-name">BrivoneÉ</span></div>
<div class="abs" style="left:180px;top:4420px;display:flex;gap:8px"><span class="social"></span><span class="social"></span><span class="social"></span><span class="social"></span></div>

<div class="abs foot-rule" style="left:407px;top:4310px;height:230px"></div>
<div class="abs foot-rule" style="left:597px;top:4310px;height:230px"></div>
<div class="abs foot-rule" style="left:813px;top:4310px;height:230px"></div>
<div class="abs foot-tick" style="left:406px;top:4308px"></div>
<div class="abs foot-tick" style="left:596px;top:4308px"></div>
<div class="abs foot-tick" style="left:812px;top:4308px"></div>

<div class="abs" style="left:460px;top:4308px"><div class="foot-head">LINKS</div><ul class="foot-list"><li>Home</li><li>About</li><li>Serives</li><li>Why choose</li><li>Blog</li><li>Contact</li></ul></div>
<div class="abs" style="left:641px;top:4308px"><div class="foot-head">SERVICES</div><ul class="foot-list"><li>Water Delivery</li><li>Water Refill</li><li>Bulk Water Services</li><li>Co-Packing</li></ul></div>
<div class="abs" style="left:860px;top:4308px;width:240px"><div class="foot-head">CONTACT</div>
  <div class="contact-row"><svg width="12" height="16" viewBox="0 0 12 16"><path d="M6 0a6 6 0 0 0-6 6c0 4.5 6 10 6 10s6-5.5 6-10a6 6 0 0 0-6-6zm0 8.5A2.5 2.5 0 1 1 6 3.5a2.5 2.5 0 0 1 0 5z" fill="var(--white)"/></svg><span>Lorem Dum street 123 LJD<br>dumy numers 463.</span></div>
  <div class="contact-row"><svg width="14" height="14" viewBox="0 0 24 24"><path d="M6.6 10.8c1.4 2.8 3.8 5.1 6.6 6.6l2.2-2.2c.3-.3.7-.4 1-.2 1.1.4 2.3.6 3.6.6.6 0 1 .4 1 1V20c0 .6-.4 1-1 1C10.6 21 3 13.4 3 4c0-.6.4-1 1-1h3.5c.6 0 1 .4 1 1 0 1.3.2 2.5.6 3.6.1.3 0 .7-.2 1L6.6 10.8z" fill="var(--white)"/></svg><span>Phone: 41 772 0365</span></div>
  <div class="contact-row"><svg width="14" height="12" viewBox="0 0 14 12"><rect x="0" y="1" width="14" height="10" rx="1" fill="var(--white)"/><path d="M0 2l7 5 7-5" stroke="var(--navy)" fill="none" stroke-width="1.4"/></svg><span>Email:info@brivonee.example</span></div>
</div>
<div class="abs" style="left:122px;top:4540px;width:945px;height:1px;background:rgba(255,255,255,.35)"></div>
<p class="abs copy">Copyright © 2025 BrivoneÉ. All Rights Reserved.</p>

</body>
</html>
```